Can you create a Business Card based on the Logo you designed.

See example and would like to see other examples.

Trying to keep it very clean with a focus on the logo and name.

```html
<!DOCTYPE html>
<html lang="en">
<head>
<meta charset="utf-8">
<title>Solvera Business Card</title>
<link rel="stylesheet" href="https://fonts.googleapis.com/css2?family=Open+Sans:wght@400;600;700&display=swap">
<style>
  :root {
    --backdrop: #959595;
    --brand-green: #0c7344;
    --leaf-green: #8bc34a;
    --sun-orange: #f4a548;
    --paper: #ffffff;
    --ink-grey: #6b6b6b;
  }
  * { margin: 0; padding: 0; box-sizing: border-box; }
  html, body {
    width: 1200px; height: 1200px; overflow: hidden;
    background: var(--backdrop);
    font-family: "Open Sans", sans-serif;
  }
  .card {
    position: absolute;
    left: 237px;
    width: 747px;
    height: 434px;
    border-radius: 22px;
    overflow: hidden;
  }
  .card-front { top: 121px; background: var(--brand-green); }
  .card-back { top: 604px; background: var(--paper); }

  .front-wordmark {
    position: absolute; inset: 0;
    display: flex; align-items: center; justify-content: center; gap: 18px;
  }
  .wordmark-dot {
    width: 30px; height: 30px; border-radius: 50%;
    background: var(--sun-orange);
  }
  .front-wordmark .wordmark-name {
    color: var(--paper); font-weight: 600; font-size: 92px; letter-spacing: -1px;
  }

  .back-details {
    position: absolute; left: 0; top: 0; width: 368px; height: 100%;
    display: flex; flex-direction: column; align-items: center;
    padding-top: 70px;
  }
  .back-wordmark { display: flex; align-items: center; gap: 10px; }
  .back-wordmark .wordmark-dot { width: 16px; height: 16px; }
  .back-wordmark .wordmark-name {
    color: var(--brand-green); font-weight: 600; font-size: 42px; letter-spacing: -0.5px;
  }
  .person-name {
    margin-top: 28px;
    color: var(--leaf-green); font-weight: 700; font-size: 29px; letter-spacing: 0.5px;
  }
  .person-title {
    margin-top: 2px;
    color: var(--sun-orange); font-weight: 600; font-size: 13px; letter-spacing: 2px;
  }
  .contact-icons {
    margin-top: 22px; display: flex; align-items: center; gap: 6px;
  }
  .icon-rule { width: 40px; height: 2px; background: var(--brand-green); margin: 0 6px; }
  .icon-badge {
    width: 30px; height: 30px; border-radius: 50%;
    background: var(--brand-green);
    display: flex; align-items: center; justify-content: center;
  }
  .contact-list {
    margin-top: 18px; list-style: none; text-align: center;
    color: var(--ink-grey); font-size: 19px; line-height: 27px;
  }
  .brand-decoration {
    position: absolute; right: 0; top: 55px; width: 415px; height: 379px;
    border-radius: 60% 0 0 0;
    background: linear-gradient(160deg, var(--sun-orange) 0%, #c6b64a 45%, var(--leaf-green) 80%);
    opacity: 0.85;
  }
</style>
</head>
<body>
  <section class="card card-front">
    <div class="front-wordmark">
      <span class="wordmark-dot"></span>
      <span class="wordmark-name">Solvera</span>
    </div>
  </section>

  <section class="card card-back">
    <div class="back-details">
      <div class="back-wordmark">
        <span class="wordmark-dot"></span>
        <span class="wordmark-name">Solvera</span>
      </div>
      <p class="person-name">MARCUS ELLERY</p>
      <p class="person-title">CHIEF EXECUTIVE OFFICER</p>
      <div class="contact-icons">
        <span class="icon-rule"></span>
        <span class="icon-badge">
          <svg width="14" height="16" viewBox="0 0 14 16"><rect x="3" y="1" width="8" height="14" rx="1.5" fill="none" stroke="#fff" stroke-width="1.6"/><circle cx="7" cy="12.5" r="0.9" fill="#fff"/></svg>
        </span>
        <span class="icon-badge">
          <svg width="16" height="12" viewBox="0 0 16 12"><rect x="1" y="1" width="14" height="10" rx="1" fill="none" stroke="#fff" stroke-width="1.5"/><path d="M1 1.5 L8 7 L15 1.5" fill="none" stroke="#fff" stroke-width="1.5"/></svg>
        </span>
        <span class="icon-badge">
          <svg width="16" height="16" viewBox="0 0 16 16" fill="none" stroke="#fff" stroke-width="1.3"><circle cx="8" cy="8" r="6.5"/><ellipse cx="8" cy="8" rx="3" ry="6.5"/><path d="M1.5 8 H14.5 M2.5 4.8 H13.5 M2.5 11.2 H13.5"/></svg>
        </span>
        <span class="icon-rule"></span>
      </div>
      <ul class="contact-list">
        <li>+1 (555) 014-2287</li>
        <li>ceo@solvera.com</li>
        <li>www.solvera.com</li>
      </ul>
    </div>
    <div class="brand-decoration" role="img" aria-label="Large brand symbol decoration in sun orange and leaf green"></div>
  </section>
</body>
</html>
```